Design website for new email startup

We are starting a company called Posta.QZ (it will live at http://posta.qz.example).

We would like the main landing page for our site designed. We have provided a very simple wireframe to help provide direction for the content it should include, but we do not expect the designers to adhere to it at all - we encourage unique ideas. There is some sample text in the wireframe - this does not have to be used, but may provide ideas.

We provide an easy way for people to manage email for a custom domain name. For example if you own "myfamilyword.example" you can point your DNS records to us and we'll make it easy to have emails addressed to your domain get forwarded to your existing email (vexmail, etc). Folks running blogs, and other small sites can quickly setup email addresses for their domains and manage them in one place.

(For technical folks, we have you point your dns mx records to us, hence the name. That way all your email hits us and we can redirect it wherever you want. We make it easy to manage a single domain or a bunch of domains. Many domain registrars offer this service for a fee, and have clumsy management tools. We provide a robust simple toolset for free, as well as premium options).

The goal of the landing page is to get folks into the signup flow. The second priority flow is to have them take a look at the premium plan offerings.

We may offer the winning designer additional work for the remainder of the site design.
Updates

I've changed this project to a committed payment.  It is no longer refundable.  Thank you.

Target Market(s)

Bloggers, podcasters, designers, app developers - people who are a little tech savvy.

Industry/Entity Type

It Company

Font styles to use
Sans Serif

Colors

Designer to choose colors to be used in the design.

Requirements
Must have
• A full fidelity mockup (comp) of the landing page including the source file (psd, ai, etc).

Some sort of logo treatment for the posta.qz brand

A call to action for signup, such as the suggested 'Get Started Here'
Nice to have
• A hip startup feel

Incorporation of the email theme

Give the impression it is simple, easy and fast

```html
<!DOCTYPE html>
<html lang="en">
<head>
<meta charset="utf-8">
<title>Posta.QZ — Email for your own domain</title>
<link rel="stylesheet" href="https://fonts.googleapis.com/css2?family=Roboto+Condensed:wght@400;700&family=Open+Sans:wght@400;600&family=Arimo:wght@400;700&display=swap">
<style>
  :root {
    --brand-blue: #1a7ec2;
    --nav-active: #1d9cec;
    --navy-button: #0f4468;
    --hero-text: #232323;
    --page-bg: #f1f1f1;
    --card-bg: #ffffff;
    --card-border: #e2e2e2;
    --icon-blue: #0fa1de;
    --body-text: #2a2a2a;
    --footer-bg: #333132;
    --footer-text: #f2f2f2;
    --footer-muted: #c9c9c9;
    --dot-active: #11a6ee;
    --dot-idle: #1a6ea3;
  }
  * { box-sizing: border-box; margin: 0; padding: 0; }
  html, body { width: 1200px; height: 845px; overflow: hidden; }
  body {
    position: relative;
    background: var(--page-bg);
    font-family: "Arimo", Arial, sans-serif;
    color: var(--body-text);
  }
  a { text-decoration: none; color: inherit; }

  .site-header {
    position: absolute; left: 0; top: 0; width: 1200px; height: 132px;
    background: var(--page-bg);
    border-top: 5px solid var(--brand-blue);
  }
  .brand {
    position: absolute; left: 142px; top: 44px;
    font-family: "Open Sans", sans-serif; font-weight: 600;
    font-size: 33px; letter-spacing: -0.5px;
    color: var(--brand-blue); text-transform: uppercase;
  }
  .main-nav {
    position: absolute; left: 685px; top: 0; width: 375px; height: 42px;
    background: var(--brand-blue); display: flex;
    font-family: "Open Sans", sans-serif; font-weight: 600; font-size: 13px;
    color: #fff;
  }
  .main-nav a { display: flex; align-items: center; justify-content: center; height: 100%; }
  .main-nav .is-active { width: 128px; background: var(--nav-active); }
  .main-nav .nav-support { width: 160px; }
  .main-nav .nav-login { width: 87px; }

  .hero {
    position: absolute; left: 0; top: 132px; width: 1200px; height: 446px;
    overflow: hidden;
  }
  .hero-visual {
    position: absolute; inset: 0;
    background:
      radial-gradient(ellipse 300px 260px at 450px 270px, rgba(222,170,150,0.75), transparent 70%),
      radial-gradient(ellipse 520px 420px at 780px 200px, #4d5a7e, transparent 75%),
      linear-gradient(90deg, #cfc9cf 0%, #a9a2b2 30%, #5d6788 60%, #6b6578 85%, #bdb4b6 100%);
    box-shadow: inset 0 3px 4px rgba(0,0,0,0.25), inset 0 -3px 4px rgba(0,0,0,0.25);
  }
  .hero-quote {
    position: absolute; left: 142px; top: 225px; width: 560px;
    font-family: "Roboto Condensed", sans-serif; font-weight: 400;
    font-size: 26px; line-height: 45px; color: var(--hero-text);
    text-transform: uppercase;
  }
  .hero-quote { top: 93px; }
  .hero-actions { position: absolute; left: 142px; top: 314px; display: flex; gap: 23px; }
  .cta {
    display: flex; align-items: center; justify-content: space-between;
    width: 181px; height: 38px; padding: 0 14px 0 13px;
    background: var(--navy-button); color: #fff; border-radius: 3px;
    box-shadow: 0 2px 3px rgba(0,0,0,0.35);
    font-family: "Roboto Condensed", sans-serif; font-weight: 700; font-size: 16px;
    text-transform: uppercase;
  }
  .cta svg { width: 19px; height: 19px; }
  .slider-dots { position: absolute; left: 561px; top: 431px; display: flex; gap: 7px; }
  .slider-dots span { width: 8px; height: 8px; background: var(--dot-idle); }
  .slider-dots .is-current { background: var(--dot-active); }

  .feature {
    position: absolute; top: 615px; width: 919px;
  }
  .feature-icon {
    position: absolute; top: 7px; width: 91px; height: 91px; border-radius: 50%;
    border: 1px solid #e3e3e3; background: #f3f3f3;
    display: flex; align-items: center; justify-content: center;
  }
  .feature-card {
    position: absolute; top: 0; width: 319px; height: 107px;
    background: linear-gradient(180deg, #fff 0%, #fff 65%, #f4f4f4 100%);
    border: 1px solid var(--card-border); padding: 10px 13px 0 13px;
  }
  .feature-card::before {
    content: ""; position: absolute; left: -9px; top: 46px;
    width: 16px; height: 16px; background: #fff;
    border-left: 1px solid var(--card-border); border-bottom: 1px solid var(--card-border);
    transform: rotate(45deg);
  }
  .feature-title {
    font-family: "Roboto Condensed", sans-serif; font-weight: 700; font-size: 14px;
    color: var(--brand-blue); text-transform: uppercase; margin-bottom: 7px;
  }
  .feature-text { font-size: 11px; line-height: 13.5px; text-align: justify; color: var(--body-text); }
  .read-more {
    display: inline-flex; align-items: center; gap: 4px; margin-top: 9px;
    font-family: "Roboto Condensed", sans-serif; font-weight: 700; font-size: 11px;
    color: var(--navy-button); text-transform: uppercase;
  }

  .site-footer {
    position: absolute; left: 0; top: 766px; width: 1200px; height: 79px;
    background: var(--footer-bg);
  }
  .footer-nav {
    position: absolute; left: 142px; top: 20px;
    font-family: "Open Sans", sans-serif; font-size: 12px; color: var(--footer-text);
  }
  .footer-nav .sep { margin: 0 5px; }
  .copyright {
    position: absolute; left: 142px; top: 46px;
    font-family: "Arimo", sans-serif; font-size: 12.5px; color: var(--footer-muted);
  }
  .social { position: absolute; left: 935px; top: 26px; display: flex; gap: 6px; }
  .social a { width: 26px; height: 26px; border-radius: 50%; background: #2b8ed1; }
</style>
</head>
<body>
  <header class="site-header">
    <a class="brand" href="http://posta.qz.example">Posta.QZ</a>
    <nav class="main-nav">
      <a class="is-active" href="#">HOW IT WORKS</a>
      <a class="nav-support" href="#">SUPPORT</a>
      <a class="nav-login" href="#">LOGIN</a>
    </nav>
  </header>

  <section class="hero">
    <div class="hero-visual" role="img" aria-label="Blurred photo of a hand touching a glowing network of connected user profile bubbles"></div>
    <p class="hero-quote">"Sed ut perspiciatis unde omnis iste natus error sit voluptatem&nbsp; ipsa quae ab illo in-<br>ventore veritatis et quasi architecto beatae vitae dicta sunt explicabo.</p>
    <div class="hero-actions">
      <a class="cta" href="#">Get started free
        <svg viewBox="0 0 20 20" aria-hidden="true"><circle cx="10" cy="10" r="9.5" fill="#c9d3da"/><path d="M8 5.5 12.5 10 8 14.5" fill="none" stroke="#0f4468" stroke-width="2.6"/></svg>
      </a>
      <a class="cta" href="#">Compare plans
        <svg viewBox="0 0 20 20" aria-hidden="true"><circle cx="10" cy="10" r="9.5" fill="#c9d3da"/><path d="M8 5.5 12.5 10 8 14.5" fill="none" stroke="#0f4468" stroke-width="2.6"/></svg>
      </a>
    </div>
    <div class="slider-dots"><span class="is-current"></span><span></span><span></span></div>
  </section>

  <article class="feature" style="left:141px">
    <div class="feature-icon" style="left:0">
      <svg width="44" height="44" viewBox="0 0 44 44" aria-hidden="true">
        <rect x="1" y="2" width="42" height="30" fill="var(--icon-blue)"/>
        <rect x="7" y="7" width="30" height="20" fill="#f3f3f3"/>
        <rect x="17" y="32" width="10" height="5" fill="var(--icon-blue)"/>
        <rect x="8" y="37" width="28" height="5" fill="var(--icon-blue)"/>
      </svg>
    </div>
    <div class="feature-card" style="left:120px">
      <h2 class="feature-title">Sed ut perspiciatis unde omnis iste natus</h2>
      <p class="feature-text">oluptatem quia voluptas sit aspernatur aut odit aut fugit, sed quia consequuntur magni dolores eos qui ratione voluptatem sequi nesciunt.</p>
      <a class="read-more" href="#">Read more <svg width="7" height="8" viewBox="0 0 7 8" aria-hidden="true"><path d="M0 0 7 4 0 8z" fill="currentColor"/></svg></a>
    </div>
  </article>

  <article class="feature" style="left:621px">
    <div class="feature-icon" style="left:0">
      <svg width="52" height="46" viewBox="0 0 52 46" aria-hidden="true">
        <rect x="2" y="4" width="30" height="20" rx="4" fill="var(--icon-blue)"/>
        <path d="M8 24 6 31 14 24z" fill="var(--icon-blue)"/>
        <rect x="20" y="18" width="30" height="20" rx="4" fill="var(--icon-blue)" stroke="#f3f3f3" stroke-width="2"/>
        <path d="M42 38 45 44 36 38z" fill="var(--icon-blue)"/>
      </svg>
    </div>
    <div class="feature-card" style="left:120px">
      <h2 class="feature-title">Sed ut perspiciatis unde omnis iste natus</h2>
      <p class="feature-text">oluptatem quia voluptas sit aspernatur aut odit aut fugit, sed quia consequuntur magni dolores eos qui ratione voluptatem sequi nesciunt.</p>
      <a class="read-more" href="#">Read more <svg width="7" height="8" viewBox="0 0 7 8" aria-hidden="true"><path d="M0 0 7 4 0 8z" fill="currentColor"/></svg></a>
    </div>
  </article>

  <footer class="site-footer">
    <nav class="footer-nav">
      <a href="#">HOW IT WORKS</a><span class="sep">|</span><a href="#">SUPPORT</a><span class="sep">|</span><a href="#">LOGIN</a>
    </nav>
    <p class="copyright">© 2014 Posta.QZ.| All Rights Reserved.</p>
    <div class="social">
      <a href="#" aria-label="Social profile 1"></a>
      <a href="#" aria-label="Social profile 2"></a>
      <a href="#" aria-label="Social profile 3"></a>
      <a href="#" aria-label="Social profile 4"></a>
    </div>
  </footer>
</body>
</html>
```